Bold Website Redesign for a Disruptive Training Brand

Brightmoor Labs is a bold, no-fluff sales & leadership training company powered by AI-driven practice and behavioral science. We’ve already built our website structure and copy in Craftly.io — now we need a designer to fully transform the visual design across all pages (Home, Approach, Programs, About, Contact).
We’re looking for a modern, memorable, high-performance aesthetic that blends human energy, science, and tech without feeling corporate or safe. Clean, bold typography, fluid layout, strong emotional hero moments, subtle motion, and imagery that mixes real people with abstract scientific/tech visuals.Because our clients are primarily North American, please ensure any human photography or AI-generated imagery reflects a North American business context and demographics (modern, diverse, and realistic).

Your job is visual redesign only — no coding required.
The final design must be practical to rebuild inside Craftly.io.

A full, detailed creative brief (plus logo files) is included in the uploaded files.
If you can bring a mix of edge, intelligence, and strong visual storytelling, we’d love to see your work.

Website is already built in Craftly.io at - https://brightmoor-website-tempdesign.craftly.app — structure is set, visuals need redesign.

```html
<!DOCTYPE html>
<html lang="en">
<head>
<meta charset="utf-8">
<title>Brightmoor Labs — Training That Practices Back</title>
<link href="https://fonts.googleapis.com/css2?family=Montserrat:ital,wght@0,300;0,400;0,500;0,600;0,700;0,800;0,900;1,400&display=swap" rel="stylesheet">
<style>
:root{
  --navy:#0b1f4d;
  --navy-deep:#081638;
  --royal:#2f4fd6;
  --cobalt:#3a5bc2;
  --sky:#41b4e8;
  --mid-blue:#3d8fd8;
  --ink:#0f2350;
  --text-grey:#5a6070;
  --rule:#2d6fc6;
  --white:#ffffff;
  --chart-bg:#f5f8fa;
  --accent-gold:#e8c21a;
}
*{margin:0;padding:0;box-sizing:border-box}
html,body{width:1200px;height:4342px;overflow:hidden}
body{font-family:'Montserrat',sans-serif;background:var(--white);position:relative;color:var(--ink)}
.abs{position:absolute}

/* HERO */
.hero{left:0;top:0;width:1200px;height:940px;background:linear-gradient(120deg,#3fc3ee 0%,#2f7fe0 35%,#2c46d4 60%,#2a2fb8 100%)}
.hero-visual{left:560px;top:160px;width:640px;height:600px;background:radial-gradient(ellipse at 60% 40%,rgba(160,190,255,.55),rgba(60,80,220,0) 65%)}
.menu-box{left:1058px;top:0;width:142px;height:126px;background:#4a6fd0;display:flex;align-items:center;justify-content:center}
.brand{left:140px;top:52px;width:230px;text-align:center;color:var(--white);font-weight:700;letter-spacing:4px;font-size:22px;line-height:1.3}
.brand small{display:block;font-size:15px;letter-spacing:6px}
.hero-copy{left:152px;top:240px;width:470px;color:var(--white)}
.hero-copy h1{font-size:49px;line-height:64px;font-weight:900;letter-spacing:1px}
.hero-copy h1 span{display:block;font-weight:400}
.hero-copy .lead{margin-top:24px;font-size:22px;font-weight:700;line-height:32px}
.hero-copy .body{margin-top:22px;font-size:16px;line-height:28px;font-weight:500}
.btn{display:inline-flex;align-items:center;justify-content:center;border-radius:32px;font-weight:700;font-size:15px;letter-spacing:.5px;height:62px}
.btn-white{position:absolute;left:152px;top:584px;width:242px;background:var(--white);color:var(--cobalt)}
.btn-outline{position:absolute;left:407px;top:584px;width:186px;border:2px solid var(--white);color:var(--white)}

/* PROBLEM */
.problem-title{left:0;top:1018px;width:1200px;text-align:center;font-size:45px;line-height:62px;color:var(--navy)}
.problem-title b{font-weight:900}
.problem-title span{display:block;font-weight:400;letter-spacing:1px}
.rule{height:3px;background:var(--rule)}
.problem-text{left:250px;top:1205px;width:700px;text-align:center;font-size:18px;line-height:34px;color:var(--text-grey)}
.chart-card{left:138px;top:1385px;width:918px;height:425px;background:var(--white);border-radius:16px;box-shadow:0 6px 30px rgba(40,80,140,.15);border:1px solid #e3eaf2}
.chart-caption{left:0;top:50px;width:918px;text-align:center;font-style:italic;font-size:13px;color:#8a8a5a}
.chart-area{left:37px;top:80px;width:845px;height:310px;background:var(--chart-bg);border-radius:12px}

/* PRACTICE */
.practice-title{left:0;top:1918px;width:1200px;text-align:center;color:var(--white);font-size:47px;letter-spacing:1px}
.practice-title b{font-weight:900}.practice-title span{font-weight:400}
.practice-sub{left:0;top:2036px;width:1200px;text-align:center;color:var(--white);font-size:18px}
.pillar{color:var(--white);font-size:13px;line-height:22px;width:200px}
.pillar h3{font-size:20px;font-weight:700;margin-bottom:8px}
.pillar-learn{left:205px;top:2124px;text-align:right}
.pillar-cert{left:784px;top:2122px}
.pillar-sustain{left:495px;top:2460px;width:232px;text-align:center}

/* TEAM */
.team-copy{left:145px;top:2774px;width:560px}
.team-copy h2{font-size:45px;line-height:60px;color:var(--navy);font-weight:900}
.team-copy h2 span{display:block;font-weight:400}
.team-copy p{margin-top:72px;font-size:18px;line-height:34px;color:var(--text-grey)}
.btn-blue{position:absolute;left:147px;top:3180px;width:243px;height:62px;background:linear-gradient(180deg,#3b8fdc,#2a5fb8);color:var(--white);box-shadow:0 4px 10px rgba(30,70,150,.3)}

/* CTA */
.cta{left:0;top:3367px;width:1200px;height:700px;background:linear-gradient(180deg,#3e8fd8,#3a7fd2)}
.cta-title{left:0;top:3455px;width:1200px;text-align:center;color:var(--white);font-weight:900;font-size:44px;line-height:62px;letter-spacing:.5px}
.btn-cta{position:absolute;left:445px;top:3612px;width:312px;height:63px;background:linear-gradient(180deg,#3c9be0,#2a6cc2);color:var(--white);box-shadow:0 4px 10px rgba(20,50,120,.3)}

/* FOOTER */
.footer-brand{left:150px;top:4070px;width:310px;text-align:center;color:var(--white);font-weight:700;font-size:32px;letter-spacing:6px;line-height:1.3}
.footer-brand small{display:block;font-size:22px;letter-spacing:9px}
.col-divider{width:1px;height:230px;background:rgba(255,255,255,.2);top:3990px}
.footer-h{font-size:16px;font-weight:800;color:var(--white);letter-spacing:.5px}
.contact-row{display:flex;align-items:center;gap:16px;color:var(--white);font-size:12.5px;line-height:17px;height:40px;margin-top:12px}
.contact-row .ico{width:34px;height:34px;border-radius:50%;border:1.5px solid var(--white);display:flex;align-items:center;justify-content:center;flex:none}
.quick a{display:block;color:var(--white);text-decoration:none;font-size:13px;line-height:27px}
.legal{left:170px;top:4280px;color:var(--white);font-size:13px}
.social{top:4272px;width:34px;height:34px;border-radius:50%;border:1.5px solid var(--white)}
</style>
</head>
<body>

<!-- HERO -->
<section class="abs hero">
  <div class="abs hero-visual" role="img" aria-label="Abstract glowing data ribbon flowing across the blue background"></div>
  <div class="abs menu-box" aria-label="Menu">
    <svg width="34" height="28" viewBox="0 0 34 28"><rect y="2" width="34" height="4" rx="2" fill="#fff"/><rect y="12" width="34" height="4" rx="2" fill="#fff"/><rect y="22" width="34" height="4" rx="2" fill="#fff"/></svg>
  </div>
  <div class="abs brand">BRIGHTMOOR<small>LABS</small></div>
  <div class="abs hero-copy">
    <h1>TRAINING THAT<span>PRACTICES BACK</span></h1>
    <p class="lead">AI-driven sustainment that builds mastery so you don't have to.</p>
    <p class="body">You'll see measurable growth as your people turn insight into habit — automatically, sustainably, and without extra work for their leaders.</p>
  </div>
  <a class="btn btn-white">SEE HOW WE DO IT</a>
  <a class="btn btn-outline">LET'S TALK</a>
</section>

<!-- chevron into white -->
<svg class="abs" style="left:0;top:700px" width="1200" height="260" viewBox="0 0 1200 260">
  <polygon points="0,225 365,20 593,155 808,20 1200,245 1200,260 0,260" fill="#fff"/>
  <polyline points="0,222 365,17 593,152 808,17 1200,242" fill="none" stroke="#3a66c8" stroke-width="9"/>
  <rect x="585" y="72" width="30" height="44" rx="15" fill="#fff"/>
  <path d="M600 83v22M593 98l7 7 7-7" stroke="#0b1f4d" stroke-width="2" fill="none"/>
</svg>

<!-- PROBLEM -->
<h2 class="abs problem-title"><b>THE REAL PROBLEM ISN'T YOUR</b><span>PEOPLE IT'S THE FORGETTING CURVE.</span></h2>
<div class="abs rule" style="left:525px;top:1160px;width:150px"></div>
<p class="abs problem-text">Within a week, most training disappears. Leaders are left guessing who's using what they learned — and no one has time to fix it. We built Brightmoor Labs to make progress automatic, measurable, and real.</p>

<!-- PRACTICE band (behind card) -->
<section class="abs" style="left:0;top:1720px;width:1200px;height:925px;background:linear-gradient(180deg,#45b2e6 0%,#3a88d4 45%,#3560c4 100%)"></section>
<svg class="abs" style="left:0;top:1715px" width="1200" height="200" viewBox="0 0 1200 200">
  <polygon points="0,0 1200,0 1200,160 1060,80 140,80 0,160" fill="#fff"/>
  <polyline points="0,160 140,80 1060,80 1200,160" fill="none" stroke="#3a66c8" stroke-width="9"/>
</svg>

<div class="abs chart-card">
  <p class="abs chart-caption">Watch how sustained practice changes the curve →</p>
  <div class="abs chart-area">
    <svg width="845" height="310" viewBox="0 0 845 310">
      <defs><linearGradient id="forgetFill" x1="0" y1="0" x2="0" y2="1"><stop offset="0" stop-color="#bfe6f2"/><stop offset="1" stop-color="#e4f5fa"/></linearGradient></defs>
      <path d="M30 90 C180 150 250 210 420 235 C560 255 680 265 820 262 L820 270 L30 270 Z" fill="url(#forgetFill)"/>
      <polyline points="30,90 110,112 190,108 265,118 340,124 430,116 520,120 600,118 690,122 770,124 820,122" fill="none" stroke="#2d5bab" stroke-width="2.5"/>
      <g fill="#2d5bab"><circle cx="110" cy="112" r="5"/><circle cx="265" cy="118" r="5"/><circle cx="420" cy="117" r="5"/><circle cx="578" cy="119" r="5"/><circle cx="735" cy="123" r="5"/></g>
      <text x="43" y="74" font-family="Montserrat,sans-serif" font-size="12" fill="#4a5060">People forget fast.</text>
      <text x="290" y="135" font-family="Montserrat,sans-serif" font-size="12" fill="#4a5060">Within a week, 70% is gone.</text>
      <text x="665" y="232" font-family="Montserrat,sans-serif" font-size="12" fill="#e8c21a">We built the fix in.</text>
    </svg>
  </div>
</div>

<!-- PRACTICE content -->
<h2 class="abs practice-title"><b>PRACTICE MADE</b> <span>PERMANENT</span></h2>
<div class="abs rule" style="left:503px;top:1998px;width:195px;background:#fff"></div>
<p class="abs practice-sub">You'll replace "hope they remember" with a system that makes sure they do.</p>

<svg class="abs" style="left:400px;top:2080px" width="400" height="380" viewBox="0 0 400 380">
  <circle cx="200" cy="175" r="162" fill="#3a5ab8"/>
  <circle cx="200" cy="175" r="122" fill="#fff" stroke="#9bb0e4" stroke-width="10"/>
  <text x="200" y="183" text-anchor="middle" font-family="Montserrat,sans-serif" font-weight="700" font-size="22" letter-spacing="2" fill="#3a5bc2">BRIGHTMOOR</text>
  <g stroke="#fff" stroke-width="2" fill="#3a5ab8">
    <circle cx="57" cy="83" r="30"/><circle cx="337" cy="83" r="30"/><circle cx="211" cy="333" r="30"/>
  </g>
  <g stroke="#fff" stroke-width="2" fill="none">
    <circle cx="57" cy="83" r="12"/><path d="M51 83h12M57 77v12"/>
    <rect x="327" y="70" width="20" height="26" rx="2"/><path d="M331 78h12M331 84h12M331 90h7"/>
    <circle cx="211" cy="333" r="13"/><path d="M198 333h26M211 320c-6 8-6 18 0 26c6-8 6-18 0-26"/>
  </g>
</svg>
<div class="abs pillar pillar-learn"><h3>Learn</h3>Fast, focused workshops, built on science, that install the mindset and skills that matter most.</div>
<div class="abs pillar pillar-cert"><h3>Certify</h3>Programmatic AI-driven practice and feedback - mastery without management overhead.</div>
<div class="abs pillar pillar-sustain"><h3>Sustain</h3>Light-touch challenges and dashboards that keep skills sharp long after training ends.</div>

<!-- TEAM -->
<div class="abs" style="left:0;top:2640px;width:738px;height:75px;background:linear-gradient(90deg,#2c3a45,#4a5d68)" role="img" aria-label="Office interior photograph strip"></div>
<div class="abs" style="left:738px;top:2640px;width:462px;height:727px;background:linear-gradient(160deg,#c9ccc6 0%,#8f8a6e 50%,#5d5a44 100%)" role="img" aria-label="Photo of a smiling professional woman presenting in an office"></div>
<div class="abs team-copy">
  <h2>BUILT BY PEOPLE<span>WHO'VE LED THE</span>CHANGE THEMSELVES</h2>
  <p>Behind Brightmoor Labs are leaders who've lived the challenge of making learning last. They've scaled companies, built cultures, and led transformation — and now they've designed the system they always wished existed.</p>
</div>
<div class="abs rule" style="left:145px;top:2983px;width:148px"></div>
<a class="btn btn-blue">MEET THE TEAM</a>

<!-- CTA -->
<section class="abs cta"></section>
<h2 class="abs cta-title">READY TO SEE WHAT LASTING<br>CAPABILITY LOOKS LIKE?</h2>
<a class="btn btn-cta">START A CONVERSATION</a>

<!-- FOOTER -->
<svg class="abs" style="left:0;top:3740px" width="1200" height="602" viewBox="0 0 1200 602">
  <polygon points="0,302 400,22 593,165 792,22 1200,290 1200,602 0,602" fill="#0b1f4d"/>
  <polyline points="0,300 400,20 593,163 792,20 1200,288" fill="none" stroke="#fff" stroke-width="10"/>
</svg>
<div class="abs footer-brand">BRIGHTMOOR<small>LABS</small></div>
<div class="abs col-divider" style="left:518px"></div>
<div class="abs col-divider" style="left:864px"></div>
<div class="abs" style="left:573px;top:4000px;width:280px">
  <p class="footer-h">CONTACT US</p>
  <div class="contact-row" style="margin-top:24px"><span class="ico"><svg width="14" height="18" viewBox="0 0 14 18"><path d="M7 1a6 6 0 0 1 6 6c0 4-6 10-6 10S1 11 1 7a6 6 0 0 1 6-6z" fill="none" stroke="#fff" stroke-width="1.6"/><circle cx="7" cy="7" r="2" fill="#fff"/></svg></span><span>4820 N Harbor Ave Suite 210<br>Tempe, AZ 85281</span></div>
  <div class="contact-row"><span class="ico" style="background:#3a66c8"><svg width="14" height="14" viewBox="0 0 14 14"><path d="M3 1l3 3-2 2c1 2 2 3 4 4l2-2 3 3-2 2C6 13 1 8 1 3z" fill="#fff"/></svg></span><b>+1 (555) 014-2290</b></div>
  <div class="contact-row"><span class="ico"><svg width="14" height="11" viewBox="0 0 14 11"><rect x="1" y="1" width="12" height="9" fill="none" stroke="#fff" stroke-width="1.4"/><path d="M1 1l6 5 6-5" fill="none" stroke="#fff" stroke-width="1.4"/></svg></span><span>hello@brightmoorlabs.com</span></div>
</div>
<div class="abs quick" style="left:926px;top:4000px">
  <p class="footer-h" style="margin-bottom:18px">QUICK LINKS</p>
  <a>Home</a><a>Approach</a><a>Programs</a><a>About</a><a>Contact</a>
</div>
<p class="abs legal">© 2025 Brightmoor Labs. All rights reserved &nbsp;|&nbsp; Privacy Policy &nbsp;|&nbsp; Terms of Use</p>
<span class="abs social" style="left:956px" aria-label="Social profile"></span>
<span class="abs social" style="left:1006px" aria-label="Social profile"></span>

</body>
</html>
```